Piano Tuning Company Needs a Postcard Design to Advertise Online Appointments

I need a postcard design for my piano tuning company. I help maintain my client's piano by tuning and doing minor repairs to increase the joy of playing their instrument. My website is now set up to book appointments online and I would like to offer $10 off of any service for making an appointment from our website, valid for 2014 only. The online booking application allows customers to see all openings on the calendar for the service they are looking for and sidesteps playing phone tag to set up an appointment. I would like to see designs that go well with the logo and its color scheme. The final design should communicate warmth, professionalism and a desire to maintain their beautiful instrument.

Target Market(s)

People who own pianos

Industry/Entity Type

It Company

Requirements
Must have
• larkwellkeys@brindlemail.net
• (425) 637-5104
• Try our online booking service and receive $10 off any service
• Offer only valid for 2014
Nice to have
• Definitely picture(s) of pianos. I have attached one that is also on my business card, but if a different picture(s) work better for your design, please feel free to use it.
• It might be nice to have something about "avoid playing phone tag, try our online service." Or there could be something about a piano needing to be tuned once a year, and when was the last time your piano was tuned?

```html
<!DOCTYPE html>
<html lang="en">
<head>
<meta charset="utf-8">
<title>Larkwell Keys – Online Booking Postcard</title>
<link rel="stylesheet" href="https://fonts.googleapis.com/css2?family=Cormorant+Garamond:ital,wght@1,500&family=Open+Sans:ital,wght@0,400;0,600;1,400;1,700&display=swap">
<style>
  :root {
    --plum: #7a1f78;
    --plum-light: #93499b;
    --cream: #f8f4ee;
    --rose: #d4195e;
    --headline: #cf2160;
    --violet-text: #6c2a7a;
    --sun: #ffe600;
    --offer-red: #d3144f;
    --white: #ffffff;
    --ink: #4a1846;
  }
  html, body {
    margin: 0;
    padding: 0;
    width: 1200px;
    height: 777px;
    overflow: hidden;
    background: var(--plum);
  }
  .postcard {
    display: block;
    width: 1200px;
    height: 777px;
  }
  .headline {
    font-family: "Cormorant Garamond", Georgia, serif;
    font-style: italic;
    font-weight: 500;
    font-size: 44px;
    fill: var(--headline);
  }
  .tagline {
    font-family: "Open Sans", Arial, sans-serif;
    font-style: italic;
    font-size: 37px;
    fill: var(--violet-text);
  }
  .offer-small {
    font-family: "Open Sans", Arial, sans-serif;
    font-style: italic;
    font-size: 20px;
    fill: var(--offer-red);
  }
  .offer-big {
    font-family: "Open Sans", Arial, sans-serif;
    font-weight: 700;
    font-size: 58px;
    fill: var(--offer-red);
    letter-spacing: -1px;
  }
  .phone {
    font-family: "Open Sans", Arial, sans-serif;
    font-size: 82px;
    fill: var(--white);
  }
  .email {
    font-family: "Open Sans", Arial, sans-serif;
    font-size: 41px;
    fill: var(--sun);
  }
  .brand-name {
    font-family: "Open Sans", Arial, sans-serif;
    font-weight: 600;
    font-size: 44px;
    fill: var(--ink);
  }
  .panel-cream { fill: var(--cream); }
  .band-light { fill: var(--plum-light); }
  .accent-line { fill: none; stroke: var(--rose); stroke-width: 5; }
  .badge { fill: var(--sun); }
  .brand-box { fill: var(--white); }
  .brand-dot { fill: var(--ink); }
</style>
</head>
<body>
<svg class="postcard" viewBox="0 0 1200 777" xmlns="http://www.w3.org/2000/svg">
  <defs>
    <clipPath id="hero-clip">
      <path d="M0 60 Q600 30 1200 42 L1200 482 Q900 525 620 512 Q300 498 0 468 Z"/>
    </clipPath>
    <linearGradient id="hero-tones" x1="0" y1="0" x2="1" y2="1">
      <stop offset="0" stop-color="#efe6d6"/>
      <stop offset="0.45" stop-color="#d9b48e"/>
      <stop offset="0.75" stop-color="#6d6470"/>
      <stop offset="1" stop-color="#1f1a1f"/>
    </linearGradient>
  </defs>

  <!-- top band -->
  <path class="band-light" d="M0 38 Q600 8 1200 22 L1200 60 Q600 48 0 74 Z"/>

  <!-- cream panel and hero area -->
  <g clip-path="url(#hero-clip)">
    <rect class="panel-cream" x="0" y="0" width="1200" height="777"/>
    <rect x="525" y="0" width="675" height="560" fill="url(#hero-tones)"
          role="img" aria-label="Photo of a smiling young girl playing a black grand piano with sheet music"/>
  </g>

  <!-- lower band accents -->
  <path class="band-light" d="M0 470 Q300 500 620 514 Q900 527 1200 484 L1200 520 Q900 560 620 548 Q300 535 0 505 Z"/>
  <path class="accent-line" d="M0 472 Q300 502 620 516 Q900 528 1200 486"/>
  <path class="band-light" d="M0 752 Q600 725 1200 748 L1200 777 L0 777 Z"/>

  <!-- headline copy -->
  <text class="headline" x="26" y="200">When was the last time</text>
  <text class="headline" x="130" y="252">your piano was tuned?</text>
  <text class="tagline" x="34" y="373">Avoid playing phone tag, try</text>
  <text class="tagline" x="118" y="424">our online service!!</text>

  <!-- offer badge -->
  <g class="badge">
    <circle cx="1041" cy="414" r="100"/>
    <circle cx="1133" cy="414" r="40"/>
    <circle cx="1115" cy="468" r="40"/>
    <circle cx="1069" cy="502" r="40"/>
    <circle cx="1013" cy="502" r="40"/>
    <circle cx="967" cy="468" r="40"/>
    <circle cx="949" cy="414" r="40"/>
    <circle cx="967" cy="360" r="40"/>
    <circle cx="1013" cy="326" r="40"/>
    <circle cx="1069" cy="326" r="40"/>
    <circle cx="1115" cy="360" r="40"/>
  </g>
  <text class="offer-small" x="1041" y="344" text-anchor="middle">Special offer !</text>
  <text class="offer-big" x="1041" y="405" text-anchor="middle">$10 off</text>
  <text class="offer-small" x="1041" y="432" text-anchor="middle">on any Service</text>
  <text class="offer-small" x="1041" y="462" text-anchor="middle">booked Online !</text>
  <text class="offer-small" x="1041" y="492" text-anchor="middle">only valid for 2014</text>

  <!-- brand block -->
  <rect class="brand-box" x="20" y="549" width="444" height="186"/>
  <circle class="brand-dot" cx="72" cy="642" r="14"/>
  <text class="brand-name" x="100" y="657">Larkwell Keys</text>

  <!-- contact -->
  <text class="phone" x="516" y="643">(425) 637-5104</text>
  <text class="email" x="520" y="699">larkwellkeys@brindlemail.net</text>
</svg>
</body>
</html>
```